Marquen Premium Men's Shaving Cream Product Label . Cream packaged in a Amber Jar/Black Top Cap.

Please include information ( see Marquen design Template attachment) designed on a Round Top cap. Label Diameter: 3.125" NOTE: Design this First,
Wrap Around Label: 11.3125 x 0.875" (w x h): NOTE: Required latter after selection of Final Design Selection.
Shave Cream packaged in an 8oz Low Profile Amber Jar/Black Top Cap.
Thanks

Target Market(s)

Prime Target-Men Ages 20yrs-65yrs+ and Women 20yrs-65yrs+( they purchase ovr 55% of these Mens care products for partner/spouse/friend.

Industry/Entity Type

Personel Care/Cosmetics/NaturalHealthcare

Other font styles liked:
• At this stage if you would like to submi a desigh that would include both a Top Label and your Wrap-around label on a Amber jar/black top lid. It would be helpful to see how it would look complete. Thanks . Please refer to the updated design Graphic Template for copy and layout . Questions? Let me know. Thanks.Please now use QUILLSTONE on label designs. Thanks! Please see image attachment for added Tree Image Vector that can be added to your design instead of the Original Tree Image .

Requirements
Must have
• Look and Feel of a Quality/Premium Mens Skincare Brand with a Masculine feel but attractive to women as well ( not Macho!).Think Unisex with a Male slant.
Nice to have
• Premium/Quality/Natural Skincare & Bodycare Brand
Should not have
• Not Macho. No Cartoony or Barber Tools/Bearded Men Images. Too gimicky and over-hyped!

```html
<!DOCTYPE html>
<html lang="en">
<head>
<meta charset="utf-8">
<title>Marquen Shaving Cream – Lid and Wrap Labels</title>
<link href="https://fonts.googleapis.com/css2?family=Montserrat:ital,wght@0,500;0,600;1,600&family=Oswald:wght@600&family=Roboto+Condensed:wght@400&display=swap" rel="stylesheet">
<style>
  :root {
    --page: #ffffff;
    --label-black: #050505;
    --ink-white: #f4f4f4;
    --olive: #8aa62a;
    --leaf: #5f8f2e;
    --leaf-deep: #3f6a22;
    --bark: #7a1e16;
    --ink-dark: #111111;
  }
  html, body {
    margin: 0;
    padding: 0;
    width: 1200px;
    height: 1122px;
    overflow: hidden;
    background: var(--page);
  }
  .canvas {
    position: relative;
    width: 1200px;
    height: 1122px;
  }

  /* ---------- Round lid label ---------- */
  .lid-label {
    position: absolute;
    left: 310px;
    top: 40px;
    width: 580px;
    height: 580px;
    border-radius: 50%;
    background: var(--label-black);
    color: var(--ink-white);
    font-family: "Montserrat", sans-serif;
  }
  .lid-ring {
    position: absolute;
    inset: 26px;
    border: 4px solid var(--olive);
    border-radius: 50%;
  }
  .lid-brand {
    position: absolute;
    top: 120px;
    left: 0;
    right: 0;
    display: flex;
    justify-content: center;
    align-items: center;
    gap: 14px;
    font-weight: 600;
    font-size: 46px;
    letter-spacing: 8px;
  }
  .brand-dot {
    width: 14px;
    height: 14px;
    border-radius: 50%;
    background: var(--ink-white);
  }
  .lid-tree {
    position: absolute;
    left: 187px;
    top: 195px;
    width: 206px;
    height: 210px;
    border-radius: 50% 50% 18% 18%;
    background: radial-gradient(circle at 50% 40%, var(--leaf) 0%, var(--leaf-deep) 60%, var(--bark) 100%);
  }
  .lid-side {
    position: absolute;
    top: 275px;
    width: 120px;
    padding: 10px 0;
    border-top: 2px solid var(--ink-white);
    border-bottom: 2px solid var(--ink-white);
    font-weight: 600;
    font-style: italic;
    font-size: 16px;
    line-height: 22px;
    text-align: center;
  }
  .lid-side.weight { left: 30px; }
  .lid-side.scent { right: 30px; }
  .lid-title {
    position: absolute;
    top: 420px;
    left: 0;
    right: 0;
    text-align: center;
    font-weight: 500;
    font-size: 28px;
    line-height: 31px;
  }

  /* ---------- Wrap-around label ---------- */
  .wrap-label {
    position: absolute;
    left: 50px;
    top: 720px;
    width: 1100px;
    height: 250px;
    background: var(--label-black);
    color: var(--ink-white);
    display: flex;
    align-items: center;
  }
  .wrap-brand {
    width: 300px;
    display: flex;
    justify-content: center;
    align-items: center;
    gap: 12px;
    font-family: "Montserrat", sans-serif;
    font-weight: 600;
    font-size: 36px;
    letter-spacing: 5px;
  }
  .wrap-copy {
    flex: 1;
    display: flex;
    flex-direction: column;
    align-items: center;
  }
  .wrap-title {
    font-family: "Oswald", sans-serif;
    font-weight: 600;
    font-size: 64px;
    line-height: 70px;
    letter-spacing: 1px;
  }
  .wrap-subtitle {
    font-family: "Roboto Condensed", sans-serif;
    font-size: 40px;
    line-height: 46px;
  }
  .wrap-scent {
    margin-top: 18px;
    padding: 4px 60px 4px 40px;
    background: var(--olive);
    border-radius: 4px 22px 4px 22px;
    color: var(--ink-dark);
    font-family: "Roboto Condensed", sans-serif;
    font-size: 28px;
  }
  .wrap-tree {
    width: 200px;
    height: 220px;
    margin-right: 20px;
    border-radius: 50% 50% 18% 18%;
    background: radial-gradient(circle at 50% 40%, var(--leaf) 0%, var(--leaf-deep) 60%, var(--bark) 100%);
  }
</style>
</head>
<body>
<main class="canvas">

  <section class="lid-label" aria-label="Round lid label">
    <div class="lid-ring"></div>
    <div class="lid-brand"><span>MARQUEN</span><span class="brand-dot"></span></div>
    <div class="lid-side weight">150G<br>E 5.3<br>oz</div>
    <div class="lid-tree" role="img" aria-label="Illustration of a tree with green leaves and red-brown branches"></div>
    <div class="lid-side scent">Emberglade<br>Reserve<br>1942</div>
    <div class="lid-title">Shaving Cream<br>Creme De<br>Rasage</div>
  </section>

  <section class="wrap-label" aria-label="Wrap-around jar label">
    <div class="wrap-brand"><span>MARQUEN</span><span class="brand-dot"></span></div>
    <div class="wrap-copy">
      <div class="wrap-title">SHAVING CREAM</div>
      <div class="wrap-subtitle">Creme De Rasage</div>
      <div class="wrap-scent">Emberglade Reserve 1942</div>
    </div>
    <div class="wrap-tree" role="img" aria-label="Illustration of a tree with green leaves and red-brown branches"></div>
  </section>

</main>
</body>
</html>
```